New Australian Event targeting the Office Industry Web Design Project

Deskora* is an exhibition and conference aimed at meeting the business needs of office professionals – the visitors are the ones that make purchase decisions when buying anything to do with the office from office equipment and stationery, event management, training and travel.

The range of exhibitors at this show is unique in Aust – therefore no other show that is similar or as relevant for this target market.
Being that it is a new show – visitors and exhibitors will want a better understanding of what the show is about, and how it is beneficial to them.

Deskora UK, Canada & US – will need to keep similar ‘brand guidelines’ but the functionality and layout is not appropriate. Eg. half a page on static banner branding is waste of space.
http://www.deskorafair.co.uk/ and www.deskoranorth.ca and http://www.deskora-expohall.com/

Some examples of Aus websites who are targeting same type of customer:
http://www.trellisfolk.com.au/
http://www.quendal.com.au/
http://www.pellowgoods.com.au/pellow/en_au/
Updates

Hi All, 

Thanks for the interest in our competition, I will be away until the 11th of January at which point i will comment on the designs. 

Thanks and Merry Xmas. 

Target Market(s)

Office Managers, Executive Assistants / Personal Assistants, Office Professionals,

Industry/Entity Type

Training

Requirements
Must have
• The website will be built into a CMS. The website will need to offer:

Homepage:
Clear CTA's - Visitor (Register free) and Exhibitor (Book a Stand)
“what’s new/hot” section on homepage
3 or 4 content areas for in-event promotions
Data capture – this will need to very visible on home page
All to fit within 'one fold'.

Content Page:
Relevant CTA's - Visitor (Register free) and Exhibitor (Book a Stand)

Sitewide:
Social media integration

I would like to see designs for a content page as well as the homepage.
Nice to have
• Floating navigation/call to action bar (top, bottom or side) - eg, http://brightlanewire.com/me/2011/12/20/sample-article-about-regional-news-sites/, http://zintaro.com/2011/12/19/photohub-2011/
Should not have
• Elements requiring Glimmerplay

```html
<!DOCTYPE html>
<html lang="en">
<head>
<meta charset="utf-8">
<title>Deskora — 12-13 September 2012, Halvern Hall, London</title>
<link rel="stylesheet" href="https://fonts.googleapis.com/css2?family=Didact+Gothic&family=Oswald:wght@400;500&family=Arimo:wght@400;700&display=swap">
<style>
:root{
  --pink:#e4147e;
  --ink:#231f20;
  --grey-panel:#e6e6e6;
  --text:#222;
  --white:#fff;
  --muted:#777;
}
*{box-sizing:border-box;margin:0;padding:0}
html,body{width:931px;height:1200px;overflow:hidden;background:var(--white)}
body{position:relative;font-family:"Arimo",Arial,sans-serif;color:var(--text)}
.abs{position:absolute}
a{color:inherit;text-decoration:none}
h2{font-weight:400}

/* header */
.brand-box{left:8px;top:0;width:201px;height:116px;background:var(--ink);border-radius:0 0 8px 8px;box-shadow:0 2px 4px rgba(0,0,0,.3);z-index:2;display:flex;align-items:center;justify-content:center}
.brand-name{font-family:"Didact Gothic",sans-serif;font-size:32px;color:var(--white);display:flex;align-items:center;gap:8px}
.brand-dot{width:10px;height:10px;background:var(--pink)}
.marker{display:block;width:6px;height:6px;border-radius:50%;background:var(--pink);margin:0 auto 6px}
.cta-top{top:54px;font-family:"Arimo",sans-serif;font-weight:700;font-size:13px;color:var(--ink);text-align:center;padding-bottom:4px;border-bottom:2px solid #bbb}
.cta-visitors{left:740px;width:68px}
.cta-exhibitor{left:845px;width:76px}

/* nav */
.main-nav{left:0;top:92px;width:931px;height:46px;background:var(--pink)}
.nav-home{left:219px;top:92px;width:69px;height:41px;background:linear-gradient(#eee,#d6d6d6);text-align:center;font-size:14px;padding-top:8px;color:var(--ink)}
.nav-item{top:108px;font-size:14px;color:var(--ink)}

/* hero */
.hero-photo{left:5px;top:148px;width:307px;height:203px;background:linear-gradient(135deg,#f2f2f2 0%,#d9d4cf 45%,#3a3a40 75%,#202228 100%)}
.hero-panel{left:312px;top:148px;width:613px;height:203px;background:var(--ink)}
.hero-rule{left:5px;top:350px;width:920px;height:5px;background:var(--pink)}
.hero-copy{left:460px;top:160px;width:360px;text-align:center;font-family:"Didact Gothic",sans-serif;font-size:24px;line-height:35px;color:var(--white)}
.hero-copy .date{color:var(--pink)}
.badge{left:334px;top:190px}
.hero-arrow{top:322px;width:22px;height:22px;background:#d0d0d0;border-radius:3px}
.hero-arrow.prev{left:854px}.hero-arrow.next{left:881px}

/* section titles */
.section-title{font-family:"Didact Gothic",sans-serif;font-size:19px;color:var(--pink)}

/* welcome */
.welcome-text{left:31px;top:413px;width:581px;font-size:12px;line-height:23.5px;text-align:justify;letter-spacing:-.2px}
.btn{font-family:"Oswald",sans-serif;font-size:12px;color:#555;text-align:center;background:linear-gradient(#fafafa,#dcdcdc);border:1px solid #c4c4c4;border-radius:4px;box-shadow:0 1px 2px rgba(0,0,0,.15);text-transform:uppercase}
.btn-more{left:520px;top:588px;width:81px;height:30px;line-height:28px}

/* events carousel */
.events-strip{left:50px;top:670px;width:580px;height:157px;background:var(--grey-panel);border-radius:8px;box-shadow:inset 0 0 0 1px #d8d8d8}
.event-card{top:680px;width:138px;height:138px;background:var(--white);border:1px solid #c9c9c9;box-shadow:0 1px 3px rgba(0,0,0,.15);display:flex;flex-direction:column;align-items:center;justify-content:center;gap:6px;font-weight:700;font-size:17px;color:var(--ink)}
.round-arrow{top:728px;width:31px;height:31px;border-radius:50%;background:var(--white);border:1px solid #ccc}

/* video */
.video-box{left:665px;top:383px;width:249px;height:188px;background:var(--ink)}
.video-bar{left:665px;top:538px;width:249px;height:33px;background:#3a3738}
.video-track{left:685px;top:550px;width:218px;height:6px;background:#222;border-radius:3px}
.video-knob{left:692px;top:546px;width:45px;height:13px;background:#eee;border-radius:6px}

/* login */
.login-panel{left:665px;top:588px;width:249px;height:169px;background:var(--grey-panel);border-radius:6px}
.oswald-pink{font-family:"Oswald",sans-serif;color:var(--pink);font-size:15px}
.check-label{top:606px;font-size:12px;color:var(--muted);display:flex;align-items:center;gap:6px}
.check-label i{width:11px;height:11px;border:1px solid #999;background:#ddd;display:inline-block}
.field{background:var(--white);border:1px solid #d3d3d3;border-radius:6px;font-size:12px;color:#999;padding-left:13px;display:flex;align-items:center}
.btn-register{left:820px;top:714px;width:80px;height:31px;line-height:29px}

/* upcoming */
.upcoming{left:665px;top:782px;width:249px;height:208px;background:var(--grey-panel)}
.upcoming-head{left:665px;top:782px;width:249px;height:31px;background:#0e0d0d}
.upcoming-title{left:684px;top:790px;font-size:14px;color:var(--pink)}
.region-select{left:828px;top:788px;width:84px;height:18px;background:#3a3a3a;border-radius:3px;font-size:12px;color:var(--white);padding-left:5px;line-height:18px}
.region-select b{position:absolute;right:3px;top:3px;width:12px;height:12px;border-radius:50%;background:#111}
.upcoming-body{left:683px;top:824px;width:228px;font-size:11.5px;line-height:23.5px;font-weight:700;color:var(--ink);white-space:nowrap}
.view-more-link{left:823px;top:959px;font-size:12px;color:var(--pink)}

/* what's new */
.news-photo{left:27px;top:884px;width:148px;height:98px;background:linear-gradient(135deg,#eef0f2 0%,#c9c3bd 45%,#2e3038 80%);border:1px solid #ccc}
.news-text{font-size:12px;line-height:17.5px;text-align:justify;color:var(--ink)}

/* query */
.label{font-size:12px;color:#555}
.input{background:var(--white);border:1px solid #cfcfcf;border-radius:4px}
.btn-submit{left:553px;top:1039px;width:80px;height:31px;line-height:29px}

/* footer */
.site-footer{left:0;top:1112px;width:931px;height:88px;background:#111}
.foot-link{top:1135px;font-size:12px;color:var(--white)}
.copyright{left:26px;top:1165px;font-size:12px;color:var(--white)}
.social{top:1128px;width:28px;height:28px;border-radius:50%}
</style>
</head>
<body>

<header>
  <div class="abs brand-box"><span class="brand-name"><span class="brand-dot"></span>Deskora</span></div>
  <a class="abs cta-top cta-visitors"><span class="marker"></span>VISITORS</a>
  <a class="abs cta-top cta-exhibitor"><span class="marker"></span>EXHIBITOR</a>
</header>

<nav>
  <div class="abs main-nav"></div>
  <a class="abs nav-home"><span class="marker"></span>Home</a>
  <a class="abs nav-item" style="left:301px">2011 Show Review</a>
  <a class="abs nav-item" style="left:434px">National PA Day 2011</a>
  <a class="abs nav-item" style="left:588px">Exhibitor</a>
  <a class="abs nav-item" style="left:665px">Visitor</a>
  <a class="abs nav-item" style="left:715px">Press</a>
  <a class="abs nav-item" style="left:770px">Venue, Travel &amp; Hotels</a>
</nav>

<section class="hero">
  <div class="abs hero-photo" role="img" aria-label="Photo of office professionals applauding at a business event"></div>
  <div class="abs hero-panel"></div>
  <svg class="abs badge" width="122" height="122" viewBox="0 0 122 122" aria-hidden="true">
    <circle cx="61" cy="61" r="58" fill="#e9e9e9" stroke="#bdbdbd" stroke-width="2"/>
    <g transform="rotate(-25 61 61)" font-family="Oswald, sans-serif" fill="#e4147e" text-anchor="middle">
      <text x="61" y="52" font-size="17">NEW VENUE</text>
      <text x="61" y="72" font-size="17">FOR</text>
      <text x="61" y="93" font-size="19">2012</text>
    </g>
  </svg>
  <p class="abs hero-copy">Your ultimate event to meet<br>and do business with<br>PAs, EAs &amp; Office Managers<br><span class="date">12 - 13 September 2012<br>Halvern Hall &nbsp;|&nbsp; London</span></p>
  <span class="abs hero-arrow prev"><svg width="22" height="22" viewBox="0 0 22 22"><path d="M11 6l-5 5 5 5M16 6l-5 5 5 5" fill="none" stroke="#fff" stroke-width="2"/></svg></span>
  <span class="abs hero-arrow next"><svg width="22" height="22" viewBox="0 0 22 22"><path d="M6 6l5 5-5 5M11 6l5 5-5 5" fill="none" stroke="#fff" stroke-width="2"/></svg></span>
  <div class="abs hero-rule"></div>
</section>

<main>
  <h2 class="abs section-title" style="left:27px;top:385px">Welcome</h2>
  <p class="abs welcome-text">Using corporate identity correctly and consistently is veryimportant. A great deal of time and consideration has been spent designing the visual aspect of the show. Keeping consistency across the material we produce will strengthen the brands value – eventhe smallest of details can make a difference.<br>Every time we use the show logo and branding, we send amessage about the quality of our services, about the value we place on the organisation and ourselves. I want people to see us as a professional organisation and, whether we are producing a document that will be seen by our own staff internally or a piece of marketing material that will be reproduced thousands of times for the public, it should be clearly branded and immediately obvious that it was produced by Corvane for the Deskora show.</p>
  <a class="abs btn btn-more">View more +</a>

  <h2 class="abs section-title" style="left:27px;top:631px">Our Latest Events</h2>
  <div class="abs events-strip"></div>
  <span class="abs round-arrow" style="left:67px"><svg width="29" height="29" viewBox="0 0 29 29"><path d="M17 9l-5 5.5 5 5.5" fill="none" stroke="#888" stroke-width="2"/></svg></span>
  <div class="abs event-card" style="left:122px"><span>Stridepost</span></div>
  <div class="abs event-card" style="left:270px"><span>Lunera</span></div>
  <div class="abs event-card" style="left:418px"><span>Tradeleaf</span><span>Inkvane</span></div>
  <span class="abs round-arrow" style="left:585px"><svg width="29" height="29" viewBox="0 0 29 29"><path d="M12 9l5 5.5-5 5.5" fill="none" stroke="#888" stroke-width="2"/></svg></span>

  <h2 class="abs section-title" style="left:27px;top:847px">What’s New?</h2>
  <div class="abs news-photo" role="img" aria-label="Photo of office professionals applauding"></div>
  <p class="abs news-text" style="left:194px;top:887px;width:149px">Lorem Ipsum is simply dummy text of the printing and typesetting industry. Lorem Ipsum has been the industry's standard dummy text ever since the 1500s,</p>
  <p class="abs news-text" style="left:27px;top:995px;width:316px">when an unknown printer took a galley of type and scrambled it to make a type specimen book.</p>

  <h2 class="abs section-title" style="left:373px;top:848px">Query Form</h2>
  <span class="abs label" style="left:373px;top:880px">Name</span>
  <span class="abs label" style="left:512px;top:880px">Email</span>
  <div class="abs input" style="left:373px;top:900px;width:122px;height:31px"></div>
  <div class="abs input" style="left:511px;top:900px;width:122px;height:31px"></div>
  <span class="abs label" style="left:372px;top:941px">Comments</span>
  <div class="abs input" style="left:371px;top:958px;width:264px;height:67px;border-radius:8px"></div>
  <a class="abs btn btn-submit">Submit</a>
</main>

<aside>
  <div class="abs video-box"></div>
  <span class="abs brand-name" style="left:732px;top:436px"><span class="brand-dot"></span>Deskora</span>
  <div class="abs video-bar"></div>
  <div class="abs video-track"></div>
  <div class="abs video-knob"></div>

  <div class="abs login-panel"></div>
  <span class="abs oswald-pink" style="left:678px;top:602px">LOGIN</span>
  <span class="abs check-label" style="left:762px"><i></i>Visitor</span>
  <span class="abs check-label" style="left:838px"><i></i>Exhibitor</span>
  <div class="abs field" style="left:677px;top:634px;width:225px;height:31px">Name......</div>
  <div class="abs field" style="left:677px;top:674px;width:225px;height:31px">Your Email......</div>
  <span class="abs oswald-pink" style="left:684px;top:720px">REGISTER FREE</span>
  <a class="abs btn btn-register">Register</a>

  <div class="abs upcoming"></div>
  <div class="abs upcoming-head"></div>
  <span class="abs upcoming-title">Up Coming Events</span>
  <span class="abs region-select">NSW<b></b></span>
  <p class="abs upcoming-body">TOVA BRENN WORKSHOP IN SYDNEY<br>TUE 14 FEB 2012, 9:00AM - 11:00AM<br>Where: TBC<br>Price: Premium members - $249.00<br>Basic members - $299.00 Table of 10 -<br>$2490.00</p>
  <a class="abs view-more-link">View More &gt;&gt;</a>
</aside>

<footer>
  <div class="abs site-footer"></div>
  <a class="abs foot-link" style="left:26px">Home</a>
  <a class="abs foot-link" style="left:81px">2011 Show Review</a>
  <a class="abs foot-link" style="left:195px">National PA Day 2011</a>
  <a class="abs foot-link" style="left:327px">Exhibitor</a>
  <a class="abs foot-link" style="left:393px">Visitor</a>
  <a class="abs foot-link" style="left:436px">Press</a>
  <a class="abs foot-link" style="left:483px">Venue, Travel &amp; Hotels</a>
  <span class="abs copyright">Copyright@2011</span>
  <span class="abs foot-link" style="left:677px">Connect With Us:</span>
  <span class="abs social" style="left:783px;background:#3b5a9a" aria-label="Social link"></span>
  <span class="abs social" style="left:818px;background:#c9c9c9" aria-label="Video channel link"></span>
  <span class="abs social" style="left:852px;background:#e0e0e0" aria-label="Photo album link"></span>
  <span class="abs social" style="left:886px;background:#4aa8dd" aria-label="News feed link"></span>
</footer>

</body>
</html>
```